Wheels Bring Trade - Two sided invitation to encourage bike friendly businesses

Pedal Haven is a charitable trust who want to grow everyday bike use. One way to do that is help businesses understand that 'Wheels Bring Trade'. We want a postcard sized 'invitation' that bike users can give to their favourite businesses, inviting them to find out more about all the benefits of attracting bike users to their business and becoming a 'Pedal Haven Business'. We are currently finalising copy, so the attached is indicative but not final copy. The docx file is the words, the png is indicative of the type of infographic we might want to feature.
I'm also attaching a mock up of our window sticker for businesses, and some social shares featuring photographic images which we have available to use. This will give you an idea of our branding to date. Our extended branding concept (which we will use when we re-do our website) is based on icons, so I'm open to seeing icon focused designs also.
The feel needs to be inviting, credible, enticing, business like, noticeable, with a strong call to action.

Target Market(s)

Small business operators: retail, cafes, etc; also managers of larger chains such as supermarkets, gyms, etc.

Industry/Entity Type

Non Profit

Font styles to use
Serif
Other font styles liked:
• Logo is done in Raleway, so need compatible font.

Colors
9ccb3b

Requirements
Must have
• Two Sides
• Use the copy provided
• Strong call to action - visiting website
• Use our colours
• A6 sized cards
Nice to have
• Compelling images and/or infographic
• Consistency with circles / curves used in other branding.
Should not have
• Not bland, not something that will get lost on the recipients desk or counter.

```html
<!DOCTYPE html>
<html lang="en">
<head>
<meta charset="utf-8">
<title>Pedal Haven – Invitation Postcard</title>
<link href="https://fonts.googleapis.com/css2?family=Oswald:wght@400;500;600&family=Open+Sans:wght@400;600;700&family=Raleway:wght@500&display=swap" rel="stylesheet">
<style>
  :root {
    --green-deep: #0f5a2a;
    --green-mid: #1e8a3c;
    --green-bright: #3aa547;
    --brand-lime: #9ccb3b;
    --orange: #f0a328;
    --white: #ffffff;
    --ink: #1d1d1d;
    --paper: #e9eaec;
    --pale: #eef3ee;
    --line: #333333;
  }
  * { box-sizing: border-box; margin: 0; padding: 0; }
  html, body { width: 1063px; height: 1200px; overflow: hidden; background: var(--paper); }
  .sheet { width: 1063px; height: 1200px; display: flex; flex-direction: column; align-items: center; justify-content: center; gap: 34px; }
  .card { position: relative; width: 800px; height: 566px; overflow: hidden; box-shadow: 0 6px 18px rgba(0,0,0,.18); }

  /* Shared brand lock-up */
  .brand { position: absolute; display: flex; align-items: center; gap: 10px; font-family: 'Raleway', sans-serif; font-weight: 500; }
  .brand__dot { width: 58px; height: 58px; border-radius: 50%; background: var(--white); border: 4px solid #cfd6cf; }
  .brand__name { background: var(--green-bright); color: var(--white); padding: 6px 22px 6px 12px; border-radius: 0 18px 18px 0; font-size: 24px; line-height: 1; }

  /* Front */
  .card--front { background: var(--green-deep); }
  .front__photo { position: absolute; inset: 0; background: radial-gradient(ellipse at 30% 40%, var(--green-bright), var(--green-mid) 45%, var(--green-deep) 100%); }
  .card--front .brand { left: 36px; top: 44px; }
  .front__url { position: absolute; left: 44px; top: 130px; font-family: 'Oswald', sans-serif; font-size: 19px; color: var(--orange); letter-spacing: .3px; }
  .headline { position: absolute; left: 44px; bottom: 42px; font-family: 'Oswald', sans-serif; color: var(--white); text-transform: uppercase; line-height: 1.08; }
  .headline__lead { font-size: 30px; font-weight: 500; }
  .headline__big { font-size: 76px; color: var(--orange); line-height: 1; font-weight: 400; }
  .headline__tail { font-size: 38px; color: var(--orange); font-weight: 500; }

  .infographic { position: absolute; right: 40px; top: 40px; width: 430px; height: 430px; }
  .infographic__ring { position: absolute; inset: 0; border-radius: 50%; background: rgba(255,255,255,.18); }
  .infographic__disc { position: absolute; inset: 22px; border-radius: 50%; background: var(--pale); }
  .infographic__car { position: absolute; left: 70px; top: 96px; width: 250px; height: 78px; border-radius: 70px 90px 18px 18px; background: linear-gradient(180deg, #f5b850, var(--orange)); }
  .infographic__car .tag { position: absolute; left: 86px; top: 22px; }
  .infographic__measure { position: absolute; left: 60px; top: 186px; width: 300px; }
  .bike-row { position: absolute; left: 60px; top: 238px; width: 250px; height: 140px; }
  .bike-slot { position: absolute; top: 0; width: 30px; height: 80px; border-radius: 15px; background: linear-gradient(180deg, #d3ddd3, #b9c8b9); }
  .bike-slot .tag { position: absolute; left: 50%; transform: translateX(-50%); }
  .bike-slot:nth-child(odd) .tag { top: 86px; }
  .bike-slot:nth-child(even) .tag { top: 108px; }
  .bike-slot:nth-child(1) { left: 0; }
  .bike-slot:nth-child(2) { left: 42px; }
  .bike-slot:nth-child(3) { left: 84px; }
  .bike-slot:nth-child(4) { left: 126px; }
  .bike-slot:nth-child(5) { left: 168px; }
  .bike-slot:nth-child(6) { left: 210px; }
  .tag { font-family: 'Open Sans', sans-serif; font-size: 10px; font-weight: 700; color: var(--green-mid); border: 1.5px solid var(--green-mid); border-radius: 6px; padding: 2px 4px; background: var(--white); white-space: nowrap; }

  .badge { position: absolute; border-radius: 50%; display: flex; flex-direction: column; align-items: center; justify-content: center; gap: 2px; font-family: 'Oswald', sans-serif; color: var(--white); border: 5px solid var(--white); line-height: 1; }
  .badge__icon { width: 30px; height: 26px; }
  .badge--car { right: -6px; top: -20px; width: 130px; height: 130px; background: var(--orange); font-size: 34px; }
  .badge--bikes { left: 312px; top: 236px; width: 140px; height: 140px; background: var(--green-deep); font-size: 36px; }

  /* Back */
  .card--back { background: var(--white); }
  .back__circle { position: absolute; right: -30px; top: -60px; width: 360px; height: 360px; border-radius: 50%; background: radial-gradient(circle at 40% 40%, var(--green-bright), var(--green-deep)); box-shadow: 0 0 0 18px var(--pale); display: flex; align-items: center; justify-content: center; }
  .back__title { font-family: 'Oswald', sans-serif; color: var(--orange); font-size: 38px; text-transform: uppercase; text-align: center; line-height: 1.1; padding: 0 30px; }
  .reasons { position: absolute; left: 44px; top: 40px; width: 400px; list-style: none; font-family: 'Open Sans', sans-serif; font-size: 17px; line-height: 1.35; color: var(--ink); counter-reset: r; }
  .reasons li { counter-increment: r; }
  .reasons li::before { content: counter(r) ". "; color: var(--green-mid); font-weight: 700; }
  .heart { color: #d8262c; }
  .back__body { position: absolute; left: 44px; top: 340px; width: 720px; font-family: 'Open Sans', sans-serif; font-size: 17px; line-height: 1.35; color: var(--ink); }
  .back__think { margin-top: 14px; font-family: 'Oswald', sans-serif; font-size: 19px; color: var(--green-mid); text-transform: uppercase; }
  .back__cta { margin-top: 12px; width: 470px; }
  .back__cta strong { color: var(--green-mid); }
  .card--back .brand { right: 40px; bottom: 36px; }
  .card--back .brand__dot { width: 48px; height: 48px; }
  .card--back .brand__name { font-size: 20px; }
</style>
</head>
<body>
<main class="sheet">
  <section class="card card--front" aria-label="Postcard front">
    <div class="front__photo" role="img" aria-label="Blurred green photograph of parked bicycles"></div>
    <div class="brand"><span class="brand__dot"></span><span class="brand__name">Pedal Haven</span></div>
    <p class="front__url">WWW.PEDALHAVEN.ORG.NZ</p>
    <h1 class="headline">
      <span class="headline__lead">Why make<br>biking customers<br>– and their $$$ –</span><br>
      <span class="headline__big">Welcome</span><br>
      <span class="headline__tail">at your business?</span>
    </h1>
    <div class="infographic">
      <div class="infographic__ring"></div>
      <div class="infographic__disc"></div>
      <div class="infographic__car" role="img" aria-label="Illustration of a car in one parking space">
        <span class="tag">$27.00</span>
      </div>
      <svg class="infographic__measure" viewBox="0 0 300 40" aria-hidden="true">
        <line x1="4" y1="28" x2="296" y2="28" stroke="#333" stroke-width="2"/>
        <line x1="4" y1="18" x2="4" y2="38" stroke="#333" stroke-width="2"/>
        <line x1="296" y1="18" x2="296" y2="38" stroke="#333" stroke-width="2"/>
        <rect x="122" y="14" width="56" height="26" fill="#eef3ee"/>
        <text x="150" y="34" text-anchor="middle" font-family="Open Sans, sans-serif" font-weight="700" font-size="16" fill="#333">13m²</text>
      </svg>
      <div class="bike-row" role="img" aria-label="Illustration of six bicycles parked in the same space, each spending $16.20 per hour">
        <div class="bike-slot"><span class="tag">$16.20</span></div>
        <div class="bike-slot"><span class="tag">$16.20</span></div>
        <div class="bike-slot"><span class="tag">$16.20</span></div>
        <div class="bike-slot"><span class="tag">$16.20</span></div>
        <div class="bike-slot"><span class="tag">$16.20</span></div>
        <div class="bike-slot"><span class="tag">$16.20</span></div>
      </div>
      <div class="badge badge--car">
        <svg class="badge__icon" viewBox="0 0 30 26" aria-hidden="true"><rect x="8" y="1" width="14" height="7" fill="#fff"/><rect x="3" y="10" width="24" height="10" rx="1" fill="#fff"/><rect x="1" y="21" width="28" height="4" fill="#fff"/></svg>
        <span>$27.00</span>
      </div>
      <div class="badge badge--bikes">
        <svg class="badge__icon" viewBox="0 0 30 26" aria-hidden="true"><rect x="8" y="1" width="14" height="7" fill="#fff"/><rect x="3" y="10" width="24" height="10" rx="1" fill="#fff"/><rect x="1" y="21" width="28" height="4" fill="#fff"/></svg>
        <span>$97.20</span>
      </div>
    </div>
  </section>

  <section class="card card--back" aria-label="Postcard back">
    <div class="back__circle" role="img" aria-label="Green photograph of a cyclist in a circle">
      <h2 class="back__title">Why welcome bikes?</h2>
    </div>
    <ol class="reasons">
      <li>Biking customers spend $$$ where parking's easy.</li>
      <li>They spend $$$ locally as they must carry what they buy.</li>
      <li>Biking customers move slower, so see what your business offers.</li>
      <li>They tell friends where's good to park and shop, where they feel welcome.</li>
      <li>You're helping people be environmentally, budget and heart friendly – and they'll <span class="heart">♥</span> you for it.</li>
    </ol>
    <div class="back__body">
      <p>A Melbourne study showed swapping a car park for six bike parks could increase the space's retail spend from $27 to $97.20 an hour.</p>
      <p class="back__think">Just think – every bike parked by someone else's business could have been your customer.</p>
      <p class="back__cta">See <strong>pedalhaven.org.nz</strong> to see how you can become a Pedal Haven Business.</p>
    </div>
    <div class="brand"><span class="brand__dot"></span><span class="brand__name">Pedal Haven</span></div>
  </section>
</main>
</body>
</html>
```